Tavosk Engineering Report Template

A word doc report Template for an Engineering Company - Tavosk

Target Market(s)

Construction/Development Industry

Industry/Entity Type

Engineering Consultant

Font styles to use
Sans Serif
Other font styles liked:
• Calibri

Colors
0455a3

Requirements
Must have
• An awesome front page, using the Tavosk Logo (not sure which version yet)
• A great back page
• Good formatting within, different heading styles which look awesome
• Format generally as the the PLW example report, no need to vary
Nice to have
• smart features? easily manipulated? not sure how tricky or smart Word is in this area.
Should not have
• LOCKED features (if possible)

```html
<!DOCTYPE html>
<html lang="en">
<head>
<meta charset="utf-8">
<title>Tavosk Engineering Report Template</title>
<link href="https://fonts.googleapis.com/css2?family=Carlito:wght@400;700&display=swap" rel="stylesheet">
<style>
:root{
  --navy:#0a1d4a;
  --deep:#0c2c6e;
  --blue:#0455a3;
  --mid:#3a7bc8;
  --light:#9dbde6;
  --pale:#dce8f6;
  --ink:#2b2f38;
  --grey:#8a919c;
  --rule:#d5dbe3;
  --paper:#ffffff;
  --bg:#ffffff;
}
*{box-sizing:border-box;margin:0;padding:0}
html,body{width:872px;height:1200px;overflow:hidden;background:var(--bg)}
body{font-family:"Carlito","Calibri",Arial,sans-serif;color:var(--ink)}
.sheet{width:872px;height:1200px;padding:22px 24px;display:grid;grid-template-columns:repeat(3,260px);grid-template-rows:repeat(3,372px);column-gap:22px;row-gap:22px}
.page{position:relative;background:var(--paper);box-shadow:0 1px 4px rgba(0,0,0,.28);overflow:hidden}
.page--dark{background:linear-gradient(160deg,var(--deep) 0%,var(--navy) 55%,#071536 100%)}
.pattern{position:absolute;inset:0;background:linear-gradient(135deg,rgba(58,123,200,.35) 0%,rgba(10,29,74,0) 45%,rgba(58,123,200,.25) 100%)}
.cover-title{position:absolute;left:18px;top:22px;color:#fff}
.cover-title h1{font-size:21px;font-weight:700;letter-spacing:.5px}
.cover-title p{font-size:8px;color:var(--light);letter-spacing:1px;margin-top:2px}
.brand{position:absolute;left:0;right:0;display:flex;flex-direction:column;align-items:center;gap:5px;color:#fff}
.brand__mark{width:24px;height:24px;background:#fff}
.brand__name{font-size:13px;font-weight:700;letter-spacing:3px}
.cover .brand{top:210px}
.cover-meta{position:absolute;left:18px;bottom:26px;color:var(--light);font-size:6px;line-height:1.5}
.band{height:44px;background:linear-gradient(120deg,var(--navy),var(--blue));position:relative;display:flex;align-items:center;justify-content:space-between;padding:0 14px}
.band h2{color:#fff;font-size:14px;font-weight:700;letter-spacing:.5px}
.band__brand{display:flex;align-items:center;gap:3px;color:#fff;font-size:6px;font-weight:700;letter-spacing:1px}
.band__brand i{width:7px;height:7px;background:#fff;display:block}
.foot{position:absolute;left:0;right:0;bottom:0;height:11px;background:var(--blue);color:#fff;font-size:5px;display:flex;justify-content:space-between;align-items:center;padding:0 12px}
.page--dark .foot{background:rgba(4,85,163,.55)}
.body{padding:12px 16px;font-size:5px;line-height:1.45;color:#555}
.toc li{list-style:none;display:flex;justify-content:space-between;border-bottom:1px dotted var(--rule);padding:3px 0;font-size:5.5px;color:var(--ink)}
.toc{margin-top:4px}
.body p{margin-bottom:5px}
.h3{font-size:7.5px;font-weight:700;color:var(--blue);margin:6px 0 3px}
.cols{display:grid;grid-template-columns:1fr 1fr;gap:10px}
.note{border-left:2px solid var(--blue);padding-left:5px;color:var(--blue);font-weight:700}
.list{padding-left:9px}
.list li{margin-bottom:2px}
.caption{font-size:5.5px;font-weight:700;color:var(--blue);margin:6px 0 3px}
table{width:100%;border-collapse:collapse;font-size:4.5px}
th{background:var(--deep);color:#fff;text-align:left;padding:2px 3px;font-weight:700}
td{padding:2px 3px;border-bottom:1px solid var(--rule)}
tr.alt td{background:var(--pale)}
.chart{display:block}
.pair{display:grid;grid-template-columns:1fr 1fr;gap:8px}
.contact{position:absolute;left:18px;top:22px;width:120px;color:#fff;font-size:5.5px;line-height:1.6}
.contact h3{font-size:7px;letter-spacing:.5px;margin-bottom:3px}
.back .brand{top:240px}
</style>
</head>
<body>
<main class="sheet">

  <!-- Cover -->
  <section class="page page--dark cover">
    <div class="pattern" role="img" aria-label="Abstract blue geometric background pattern"></div>
    <div class="cover-title"><h1>PROJECT TITLE</h1><p>PROJECT SUBTITLE</p></div>
    <div class="brand"><span class="brand__mark"></span><span class="brand__name">TAVOSK</span></div>
    <div class="cover-meta">Date: 00 Month 2024<br>Version: 01</div>
    <div class="foot"><span>Tavosk Engineering</span><span></span></div>
  </section>

  <!-- Contents -->
  <section class="page">
    <header class="band"><h2>CONTENTS</h2><span class="band__brand"><i></i>TAVOSK</span></header>
    <div class="body">
      <ul class="toc">
        <li><span>Introduction</span><span>03</span></li>
        <li><span>Text</span><span>03</span></li>
        <li><span>Text (continued)</span><span>04</span></li>
        <li><span>Tables</span><span>05</span></li>
        <li><span>Bar charts</span><span>06</span></li>
        <li><span>Line charts</span><span>07</span></li>
        <li><span>Charts (continued)</span><span>08</span></li>
      </ul>
    </div>
    <div class="foot"><span>Tavosk Engineering</span><span>02</span></div>
  </section>

  <!-- Text -->
  <section class="page">
    <header class="band"><h2>TEXT</h2><span class="band__brand"><i></i>TAVOSK</span></header>
    <div class="body">
      <p>This report sets out the scope, method and findings of the project. Body text uses a clear sans serif at a readable size with generous spacing between lines and paragraphs for easy review.</p>
      <p>Each section opens with a short summary, followed by detail, tables and charts that support the key points raised by the engineering team.</p>
      <p>Headings, captions and notes follow a consistent style so the document stays easy to edit and simple to navigate.</p>
      <div class="cols">
        <div>
          <div class="h3">First heading goes here</div>
          <p>Text under a first level heading introduces a topic and explains its purpose within the wider report for the client.</p>
          <p>Keep paragraphs short and direct so that readers can scan the content quickly.</p>
          <div class="h3">Second heading</div>
          <p>A second level heading breaks a topic into smaller parts with its own text.</p>
        </div>
        <div>
          <p>Site conditions, loads and constraints are described here along with any assumptions made during design.</p>
          <p class="note">Highlighted notes draw attention to key risks or actions.</p>
          <p>Further detail can follow in the next section of the report.</p>
        </div>
      </div>
    </div>
    <div class="foot"><span>Tavosk Engineering</span><span>03</span></div>
  </section>

  <!-- Text continued -->
  <section class="page">
    <header class="band"><h2>TEXT (CONT'D)</h2><span class="band__brand"><i></i>TAVOSK</span></header>
    <div class="body">
      <div class="h3">Bulleted text</div>
      <ul class="list">
        <li>First bullet point with a short line of text</li>
        <li>Second bullet point that runs a little longer across the page</li>
        <li>Third bullet point
          <ul class="list"><li>Sub point one</li><li>Sub point two</li></ul>
        </li>
        <li>Final bullet point in this list</li>
      </ul>
      <div class="h3">Numbered text</div>
      <ol class="list">
        <li>First numbered step in the process</li>
        <li>Second numbered step with more detail</li>
        <li>Third numbered step
          <ol class="list" type="a"><li>Sub step one</li><li>Sub step two</li></ol>
        </li>
        <li>Final numbered step</li>
      </ol>
    </div>
    <div class="foot"><span>Tavosk Engineering</span><span>04</span></div>
  </section>

  <!-- Tables -->
  <section class="page">
    <header class="band"><h2>TABLES</h2><span class="band__brand"><i></i>TAVOSK</span></header>
    <div class="body">
      <div class="caption">Table style 1</div>
      <table><tr><th>Item</th><th>Qty</th><th>Unit</th><th>Total</th></tr>
        <tr><td>Row one</td><td>10</td><td>m</td><td>100</td></tr>
        <tr class="alt"><td>Row two</td><td>12</td><td>m</td><td>144</td></tr>
        <tr><td>Row three</td><td>8</td><td>m</td><td>64</td></tr></table>
      <div class="caption">Table style 2</div>
      <table><tr><th>Item</th><th>Qty</th><th>Unit</th><th>Total</th></tr>
        <tr class="alt"><td>Row one</td><td>4</td><td>t</td><td>16</td></tr>
        <tr><td>Row two</td><td>6</td><td>t</td><td>36</td></tr>
        <tr class="alt"><td>Row three</td><td>9</td><td>t</td><td>81</td></tr></table>
      <div class="caption">Table style 3</div>
      <table><tr><th>Item</th><th>Value</th></tr>
        <tr><td>Row one</td><td>2.5</td></tr>
        <tr><td>Row two</td><td>3.1</td></tr></table>
      <div class="caption">Table style 4</div>
      <table><tr><th>Item</th><th>Value</th></tr>
        <tr class="alt"><td>Row one</td><td>1.8</td></tr>
        <tr class="alt"><td>Row two</td><td>4.0</td></tr></table>
    </div>
    <div class="foot"><span>Tavosk Engineering</span><span>05</span></div>
  </section>

  <!-- Bar charts -->
  <section class="page">
    <header class="band"><h2>BAR CHARTS</h2><span class="band__brand"><i></i>TAVOSK</span></header>
    <div class="body">
      <div class="caption">Chart style 1</div>
      <svg class="chart" width="228" height="70" viewBox="0 0 228 70">
        <line x1="10" y1="62" x2="224" y2="62" stroke="#d5dbe3"/>
        <g fill="#0c2c6e"><rect x="20" y="30" width="8" height="32"/><rect x="70" y="20" width="8" height="42"/><rect x="120" y="35" width="8" height="27"/><rect x="170" y="15" width="8" height="47"/></g>
        <g fill="#3a7bc8"><rect x="30" y="40" width="8" height="22"/><rect x="80" y="28" width="8" height="34"/><rect x="130" y="25" width="8" height="37"/><rect x="180" y="30" width="8" height="32"/></g>
        <g fill="#9dbde6"><rect x="40" y="48" width="8" height="14"/><rect x="90" y="42" width="8" height="20"/><rect x="140" y="45" width="8" height="17"/><rect x="190" y="38" width="8" height="24"/></g>
      </svg>
      <div class="caption">Chart style 2</div>
      <svg class="chart" width="228" height="70" viewBox="0 0 228 70">
        <line x1="40" y1="4" x2="40" y2="66" stroke="#d5dbe3"/>
        <g fill="#0c2c6e"><rect x="40" y="8" width="120" height="6"/><rect x="40" y="24" width="90" height="6"/><rect x="40" y="40" width="150" height="6"/><rect x="40" y="56" width="70" height="6"/></g>
        <g fill="#3a7bc8"><rect x="40" y="14" width="80" height="5"/><rect x="40" y="30" width="110" height="5"/><rect x="40" y="46" width="60" height="5"/><rect x="40" y="62" width="100" height="4"/></g>
        <g font-size="5" fill="#8a919c"><text x="8" y="17">Item A</text><text x="8" y="33">Item B</text><text x="8" y="49">Item C</text><text x="8" y="64">Item D</text></g>
      </svg>
      <div class="pair">
        <div><div class="caption">Chart style 3</div>
          <svg class="chart" width="110" height="80" viewBox="0 0 110 80">
            <g fill="#0c2c6e"><rect x="24" y="6" width="60" height="8"/><rect x="24" y="26" width="80" height="8"/><rect x="24" y="46" width="45" height="8"/><rect x="24" y="66" width="70" height="8"/></g>
            <g fill="#9dbde6"><rect x="84" y="6" width="14" height="8"/><rect x="69" y="46" width="20" height="8"/></g>
          </svg></div>
        <div><div class="caption">Chart style 4</div>
          <svg class="chart" width="110" height="80" viewBox="0 0 110 80">
            <g fill="#3a7bc8"><rect x="24" y="6" width="50" height="8"/><rect x="24" y="26" width="72" height="8"/><rect x="24" y="46" width="38" height="8"/><rect x="24" y="66" width="60" height="8"/></g>
          </svg></div>
      </div>
    </div>
    <div class="foot"><span>Tavosk Engineering</span><span>06</span></div>
  </section>

  <!-- Line charts -->
  <section class="page">
    <header class="band"><h2>LINE CHARTS</h2><span class="band__brand"><i></i>TAVOSK</span></header>
    <div class="body">
      <div class="caption">Chart style 1</div>
      <svg class="chart" width="228" height="80" viewBox="0 0 228 80">
        <g stroke="#e3e8ee"><line x1="10" y1="15" x2="224" y2="15"/><line x1="10" y1="40" x2="224" y2="40"/><line x1="10" y1="65" x2="224" y2="65"/></g>
        <polyline fill="none" stroke="#0c2c6e" stroke-width="1.5" points="10,40 60,34 110,44 160,30 224,36"/>
        <polyline fill="none" stroke="#3a7bc8" stroke-width="1.5" points="10,52 60,48 110,55 160,46 224,50"/>
        <polyline fill="none" stroke="#9dbde6" stroke-width="1.5" points="10,28 60,24 110,30 160,22 224,26"/>
      </svg>
      <div class="caption">Chart style 2</div>
      <svg class="chart" width="228" height="80" viewBox="0 0 228 80">
        <polygon fill="#9dbde6" points="10,72 10,50 60,40 110,46 160,30 224,36 224,72"/>
        <polygon fill="#3a7bc8" points="10,72 10,58 60,50 110,54 160,44 224,48 224,72"/>
        <polygon fill="#0c2c6e" points="10,72 10,64 60,60 110,62 160,56 224,60 224,72"/>
      </svg>
      <div class="pair">
        <div><div class="caption">Chart style 3</div>
          <svg class="chart" width="110" height="70" viewBox="0 0 110 70">
            <polygon fill="#0455a3" points="0,68 0,50 30,20 60,35 110,5 110,68"/>
          </svg></div>
        <div><div class="caption">Chart style 4</div>
          <svg class="chart" width="110" height="70" viewBox="0 0 110 70">
            <polygon fill="#9dbde6" points="0,68 0,30 40,20 80,40 110,25 110,68"/>
            <polygon fill="#0c2c6e" points="0,68 0,50 40,44 80,55 110,45 110,68"/>
          </svg></div>
      </div>
    </div>
    <div class="foot"><span>Tavosk Engineering</span><span>07</span></div>
  </section>

  <!-- Pie charts -->
  <section class="page">
    <header class="band"><h2>CHARTS (CONT'D)</h2><span class="band__brand"><i></i>TAVOSK</span></header>
    <div class="body">
      <div class="caption">Chart style 1</div>
      <svg class="chart" width="228" height="110" viewBox="0 0 228 110">
        <circle cx="114" cy="55" r="50" fill="#9dbde6"/>
        <path d="M114 55 L114 5 A50 50 0 0 1 160 74 Z" fill="#0c2c6e"/>
        <path d="M114 55 L160 74 A50 50 0 0 1 80 92 Z" fill="#3a7bc8"/>
      </svg>
      <div class="pair">
        <div><div class="caption">Chart style 2</div>
          <svg class="chart" width="110" height="100" viewBox="0 0 110 100">
            <circle cx="55" cy="50" r="38" fill="#dce8f6"/>
            <path d="M55 50 L55 12 A38 38 0 1 1 19 62 Z" fill="#3a7bc8"/>
            <path d="M55 50 L19 62 A38 38 0 0 1 28 23 Z" fill="#0c2c6e"/>
          </svg></div>
        <div><div class="caption">Chart style 3</div>
          <svg class="chart" width="110" height="100" viewBox="0 0 110 100">
            <circle cx="55" cy="50" r="32" fill="none" stroke="#dce8f6" stroke-width="12"/>
            <circle cx="55" cy="50" r="32" fill="none" stroke="#0455a3" stroke-width="12" stroke-dasharray="140 201" transform="rotate(-90 55 50)"/>
          </svg></div>
      </div>
    </div>
    <div class="foot"><span>Tavosk Engineering</span><span>08</span></div>
  </section>

  <!-- Back page -->
  <section class="page page--dark back">
    <div class="pattern" role="img" aria-label="Abstract blue geometric background pattern"></div>
    <div class="contact">
      <h3>CONTACT DETAILS</h3>
      <p>Phone: 01 2345 6789</p>
      <p>Email: info@tavosk.example</p>
      <p>Web: www.tavosk.example</p>
      <p>Address: 12 Sample Street, Town</p>
    </div>
    <div class="brand"><span class="brand__mark"></span><span class="brand__name">TAVOSK</span></div>
    <div class="foot"><span>Tavosk Engineering</span><span></span></div>
  </section>

</main>
</body>
</html>
```